Plakat-Design gegen antimuslimischen Rassismus - Haltestelle
Zielgruppe
Antirassismus Organisation, wir möchten auf den steigenden Rassismus aufmerksam machen. Es soll ein Straßenbahn-Wartehallenplakat designed werden, das:
1. darauf aufmerksam macht das in der Nähe eine sichtbare Muslimin aus rassistischen Gründen verprügelt wurde (Kopftuchtragende Muslimin). Schockeffekt. Siehe unten.
2. Das der Rassismus täglich zunimmt und wir alle gemeinsam dagegen ankämpfen müssen.
Auf dem Design: Soll ein Angriff auf eine sichtbare Muslimin dargestellt werden und ein Hinweis mit STOP, desweiteren ein Satz mit einem Hinweis: Stopp dem antimuslimischen Rassismus. Ein kleines Textfeld in dem erklärt wird: Das hier in der Nähe einer muslimischen Frau Gewalt angetan worden ist.
Das Plakat soll vor allem viral gehen und zum Nachdenken animieren.
Die Hintergrundgeschichte des Plakates:
Gegen 15:30 bei der Bushaltestelle 21C Heinsstrasse / Ecke Pöchwanderstrasse ereignete sich ein besonders hinterhältiger rassistischer Angriff.
Leyla K. fuhr mit dem 21C gerade nach Hause als sie bemerkte wie eine Dame ihre Gehhilfe auf den Boden fallen ließ. Sie eilte herbei um der älteren Dame behilflich zu sein und bückte sich um den Krückstock aufzuheben. Statt Dankbarkeit zu zeigen, schlug die Frau mit ihrem zweiten Krückstock mit voller Wucht auf den Kopf von Leyla K. mehrere Male ein. Leyla K. wurde schwarz vor Augen und musste mit der Rettung ins Krankenhaus befördert werden.
Vor der Polizei noch schrie die ältere Rassistin, dass sie die Tat nicht bereuen würde und immer wieder auf Ausländer einschlagen würde. Die Dame schien bereits zuvor tätige Angriffe auf MuslimInnen getätigt zu haben, entkam aber laut unseren Informationen ohne strafrechtlicher Ahndung.
Zahlreiche Zeugen aus dem Bus sagten gegen die gewalttätige Rassistin aus. Ein autochthones Ehepaar kam Leyla K. als erstes zur Hilfe, auch sie wurde von der Täterin verbal attackiert: 'Sie seien doch ebenso Österreicher, wieso sie nic..
Aufgabenstellung
Das Format des Wartehallenplakates ist: 24-Bogen Plakat 504 cm x 238 cm

```html
<!DOCTYPE html>
<html lang="de">
<head>
<meta charset="utf-8">
<title>Stopp dem antimuslimischen Rassismus – Wartehallenplakat</title>
<link rel="stylesheet" href="https://fonts.googleapis.com/css2?family=Anton&family=Carlito&display=swap">
<style>
  :root {
    --bg-mauve: #b89daf;
    --ink: #0a0a0a;
    --alert-red: #fe0000;
    --panel-white: #ffffff;
  }
  html, body {
    margin: 0;
    padding: 0;
    overflow: hidden;
  }
  .poster {
    position: relative;
    width: 1200px;
    height: 567px;
    background: var(--bg-mauve);
    overflow: hidden;
  }
  .figure-art {
    position: absolute;
    left: 108px;
    top: 28px;
    width: 289px;
    height: 413px;
  }
  .stop-mark {
    position: absolute;
    left: 146px;
    top: 268px;
    margin: 0;
    font-family: "Anton", "Arial Black", sans-serif;
    font-size: 86px;
    line-height: 1;
    color: var(--alert-red);
    letter-spacing: 1px;
  }
  .exclaim-dot {
    position: absolute;
    left: 201px;
    top: 461px;
    width: 90px;
    height: 90px;
  }
  .headline {
    position: absolute;
    left: 420px;
    top: 22px;
    margin: 0;
    font-family: "Anton", "Arial Black", sans-serif;
    font-weight: 400;
    font-size: 86px;
    line-height: 93px;
    color: var(--ink);
    letter-spacing: 0.5px;
  }
  .info-panel {
    position: absolute;
    left: 594px;
    top: 301px;
    width: 606px;
    height: 266px;
    box-sizing: border-box;
    background: var(--panel-white);
    border-top: 2px solid var(--ink);
    border-left: 2px solid var(--ink);
    padding: 14px 0 0 27px;
  }
  .info-text {
    margin: 0;
    font-family: "Carlito", "Calibri", sans-serif;
    font-size: 22px;
    line-height: 30px;
    color: var(--ink);
    white-space: nowrap;
  }
</style>
</head>
<body>
<main class="poster">
  <svg class="figure-art" role="img" aria-label="Illustration: Silhouette einer kopftuchtragenden Muslimin mit Verletzungen und Bluttränen" viewBox="0 0 289 413">
    <defs>
      <linearGradient id="figureTone" x1="0" y1="0" x2="0" y2="1">
        <stop offset="0" stop-color="#1a1a1a"/>
        <stop offset="1" stop-color="#0a0a0a"/>
      </linearGradient>
    </defs>
    <rect x="0" y="0" width="289" height="413" rx="12" fill="url(#figureTone)"/>
  </svg>
  <p class="stop-mark">STOP</p>
  <svg class="exclaim-dot" viewBox="0 0 90 90" aria-hidden="true">
    <circle cx="45" cy="45" r="45" fill="var(--ink)"/>
  </svg>

  <h1 class="headline">Stopp dem<br>antimuslimischen<br>Rassismus!</h1>

  <section class="info-panel">
    <p class="info-text">Die Muslimin Leyla K. wird nachts Opfer eines<br>hinterhältigen Attentats. Diese rassistische und<br>unmenschliche Tat geschah nicht weit von hier.<br>Solche Übergriffe sind in Deutschland mittlerweile an<br>der Tagesordnung!<br>Nur gemeinsam können wir den wachsenden<br>Rassismus in Deutschland stoppen, damit Menschen<br>wie Leyla wieder sicher das Haus verlassen können.</p>
  </section>
</main>
</body>
</html>
```